IT Company requires new Business Card design.

Over the years we have had a few different business card designs. We are now due for new cards across the board for all staff. We felt this would be a good time to start fresh with a new design. Our traditional card simply had our details on the front, and a list of services on the back. We don't particularly need the list of services, we have had cards where the only thing on the rear of the card was our logo.
Feel free to be creative, we would like our tag line "Complete IT Management" to appear at some point, doesn't necessarily have to be with the logo.
I have attached samples and drafts of various previous cards we have used over the years.
Industry/Entity Type
Business
Look and feel
Each slider illustrates characteristics of the customer's brand and the style your logo design should communicate.

```html
<!DOCTYPE html>
<html lang="en">
<head>
<meta charset="utf-8">
<title>Ridgeway Systems – Business Card</title>
<link href="https://fonts.googleapis.com/css2?family=Questrial&display=swap" rel="stylesheet">
<style>
  :root {
    --stage: #2b2b2b;
    --slate: #5b6c79;
    --slate-dark: #4a5a67;
    --paper: #f4f4f4;
    --white: #ffffff;
    --muted: #3f4a52;
  }
  * { box-sizing: border-box; margin: 0; padding: 0; }
  html, body {
    width: 1200px; height: 900px; overflow: hidden;
    background: var(--stage);
    font-family: "Questrial", "Century Gothic", sans-serif;
  }
  .stage {
    width: 1200px; height: 900px;
    display: flex; align-items: center; justify-content: center; gap: 50px;
  }
  .card {
    width: 525px; height: 300px;
    position: relative;
    box-shadow: 0 10px 30px rgba(0,0,0,.45);
  }

  /* Back of card */
  .card--back {
    background: var(--slate);
    display: flex; align-items: center; justify-content: center;
  }
  .brand {
    display: flex; align-items: center; gap: 16px;
  }
  .brand__mark {
    width: 22px; height: 22px; background: currentColor;
  }
  .brand__text { display: flex; flex-direction: column; }
  .brand__name {
    font-size: 40px; line-height: 1; text-transform: uppercase; letter-spacing: 1px;
  }
  .brand__tagline {
    font-size: 11px; text-transform: uppercase; letter-spacing: 3.6px; margin-top: 6px;
  }
  .card--back .brand { color: var(--white); }

  /* Front of card */
  .card--front {
    background: var(--paper);
    color: var(--slate);
  }
  .card--front .brand {
    position: absolute; top: 40px; left: 0; right: 0; justify-content: center;
  }
  .card--front .brand__name { font-size: 30px; }
  .card--front .brand__mark { width: 16px; height: 16px; }
  .card--front .brand__tagline { font-size: 8.5px; letter-spacing: 2.8px; }

  .details {
    position: absolute; top: 125px; left: 30px; right: 24px;
    display: flex; align-items: center;
  }
  .person {
    display: flex; align-items: center; gap: 9px;
    width: 200px; color: var(--muted);
  }
  .person__icon { width: 22px; height: 22px; flex: none; }
  .person__name { font-size: 17px; line-height: 1; text-transform: uppercase; }
  .person__role { font-size: 14px; line-height: 1.1; }

  .divider {
    width: 1.5px; height: 84px; background: var(--slate); margin: 0 16px 0 6px;
  }
  .contact { list-style: none; font-size: 11.5px; color: var(--muted); }
  .contact li { display: flex; align-items: flex-start; gap: 6px; line-height: 1.5; }
  .contact svg { width: 12px; height: 12px; flex: none; margin-top: 3px; }

  .web {
    position: absolute; bottom: 26px; left: 0; right: 0; text-align: center;
    font-size: 14px; color: var(--slate);
  }
</style>
</head>
<body>
<main class="stage">

  <section class="card card--back" aria-label="Card back">
    <div class="brand">
      <span class="brand__mark"></span>
      <div class="brand__text">
        <span class="brand__name">Ridgeway Systems</span>
        <span class="brand__tagline">Complete IT Management</span>
      </div>
    </div>
  </section>

  <section class="card card--front" aria-label="Card front">
    <div class="brand">
      <span class="brand__mark"></span>
      <div class="brand__text">
        <span class="brand__name">Ridgeway Systems</span>
        <span class="brand__tagline">Complete IT Management</span>
      </div>
    </div>

    <div class="details">
      <div class="person">
        <svg class="person__icon" viewBox="0 0 24 24" aria-hidden="true">
          <circle cx="12" cy="12" r="12" fill="var(--slate)"/>
          <circle cx="12" cy="9" r="4" fill="var(--paper)"/>
          <path d="M5 19c1.5-3.5 4-5 7-5s5.5 1.5 7 5" fill="var(--paper)"/>
        </svg>
        <div>
          <div class="person__name">Your Name</div>
          <div class="person__role">Company Position</div>
        </div>
      </div>

      <span class="divider"></span>

      <ul class="contact">
        <li>
          <svg viewBox="0 0 12 12" aria-hidden="true"><circle cx="6" cy="6" r="5.4" fill="none" stroke="var(--slate)"/><path d="M4 3.2l1 1.4-.6.7c.4.9 1 1.5 1.9 1.9l.7-.6 1.4 1-.5 1c-2.5-.3-4.2-2-4.5-4.5z" fill="var(--slate)"/></svg>
          <span>08 5550 1230</span>
        </li>
        <li>
          <svg viewBox="0 0 12 12" aria-hidden="true"><circle cx="6" cy="6" r="5.4" fill="none" stroke="var(--slate)"/><rect x="3" y="5" width="6" height="3" fill="var(--slate)"/><rect x="4" y="3" width="4" height="2" fill="none" stroke="var(--slate)" stroke-width=".7"/></svg>
          <span>08 5550 1232</span>
        </li>
        <li>
          <svg viewBox="0 0 12 12" aria-hidden="true"><circle cx="6" cy="6" r="5.4" fill="none" stroke="var(--slate)"/><rect x="3" y="4" width="6" height="4" fill="var(--slate)"/><path d="M3 4l3 2.2L9 4" fill="none" stroke="var(--paper)" stroke-width=".6"/></svg>
          <span>support@ridgewaysystems.com.au</span>
        </li>
        <li>
          <svg viewBox="0 0 12 12" aria-hidden="true"><circle cx="6" cy="6" r="5.4" fill="none" stroke="var(--slate)"/><path d="M3 6.2L6 3.4l3 2.8H8v2.5H4V6.2z" fill="var(--slate)"/></svg>
          <span>Unit 4, 12 Marlow Street, Brookfield<br>WA 6000</span>
        </li>
      </ul>
    </div>

    <p class="web">web@ridgewaysystems.com.au</p>
  </section>

</main>
</body>
</html>
```